Need a flyer to leave behind when visiting clients or at shows

Glossy colorful tri-fold flyer with the same information that is on my web site www.brevalinkpro.com. I am open to a little modern or creative take on the typical brochure. I created the web site so I can provide any raw files needed from it. I would also like the ability to edit this flyer in the future in Adobe Photoshop Elements

```html
<!DOCTYPE html>
<html lang="en">
<head>
<meta charset="utf-8">
<title>BrevaLink Pro Solutions – Tri-fold Brochure</title>
<link href="https://fonts.googleapis.com/css2?family=Ubuntu:ital,wght@0,500;0,700;1,700&family=Open+Sans:wght@400;600&display=swap" rel="stylesheet">
<style>
  :root{
    --purple:#6b3fa9;
    --purple-deep:#5a2f96;
    --purple-soft:#8a63c4;
    --paper:#ffffff;
    --ink:#2d2d33;
    --muted:#55555e;
    --backdrop:#e4e4e6;
  }
  *{box-sizing:border-box;margin:0;padding:0}
  html,body{width:933px;height:1200px;overflow:hidden;background:var(--backdrop)}
  body{position:relative;font-family:"Open Sans",sans-serif;color:var(--ink)}
  .sheet{position:absolute;left:20px;width:893px;height:560px;background:var(--paper);display:flex;box-shadow:0 6px 18px rgba(0,0,0,.18)}
  .sheet--outside{top:24px}
  .sheet--inside{top:616px}
  .panel{position:relative;width:297.67px;height:100%;overflow:hidden}
  .panel + .panel{border-left:1px solid #eee}
  .photo{position:absolute;display:block}
  .wave{position:absolute;left:0;width:100%;display:block}
  h2{font-family:"Ubuntu",sans-serif;font-weight:700;font-style:italic}
  h3{font-family:"Ubuntu",sans-serif;font-weight:700;font-style:italic;font-size:15px;color:var(--ink)}

  /* outside – about panel */
  .about-tab{position:absolute;left:22px;top:262px;background:var(--purple);color:#fff;font-size:20px;padding:6px 22px 6px 16px;border-radius:0 14px 0 0}
  .about-body{position:absolute;left:30px;top:318px;right:22px}
  .about-body p{font-size:10.5px;color:var(--muted);line-height:1.35;margin:3px 0 14px}
  .about-body .leader{font-size:11px;color:var(--ink)}
  .about-body .leader b{font-weight:600}

  /* outside – contact panel */
  .badge{position:absolute;left:50%;top:28px;width:62px;height:44px;margin-left:-31px;border-radius:50%;background:#c8c8d0}
  .contact{position:absolute;left:0;right:0;top:330px;bottom:0;background:var(--purple);color:#fff;padding:36px 30px}
  .contact h2{font-style:normal;font-size:25px;margin-bottom:8px}
  .contact .phone{display:flex;align-items:center;gap:6px;font-family:"Ubuntu",sans-serif;font-weight:700;font-size:24px}
  .contact .email{display:flex;align-items:center;gap:8px;font-size:12px;margin-top:14px}

  /* outside – cover panel */
  .brand{position:absolute;right:0;top:0;width:220px;height:88px;background:var(--purple);border-radius:0 0 0 40px;display:flex;align-items:center;justify-content:center;gap:8px}
  .brand-mark{width:12px;height:12px;background:#fff}
  .brand-name{font-family:"Ubuntu",sans-serif;font-weight:700;font-size:19px;color:#fff}
  .headline{position:absolute;left:24px;right:18px;top:150px}
  .headline h1{font-family:"Ubuntu",sans-serif;font-weight:700;font-size:19px;line-height:1.15;color:var(--purple)}
  .headline p{font-size:10px;color:var(--ink);margin-top:8px;line-height:1.3}

  /* inside – bio panel */
  .bio{position:absolute;left:0;right:0;top:250px;bottom:0;background:var(--purple);color:#fff;padding:16px 22px}
  .bio-head{display:flex;gap:12px;align-items:flex-start;height:76px}
  .portrait{width:74px;height:76px;border-radius:12px;background:linear-gradient(160deg,#b9b2c4,#5e5668);flex:none}
  .bio-name{font-family:"Ubuntu",sans-serif;font-style:italic;font-weight:700;font-size:12px}
  .bio-name small{font-size:9px;font-weight:500}
  .bio-role{font-size:9px;font-weight:600;margin-top:1px}
  .bio-badge{width:50px;height:34px;border-radius:50%;background:#d7d2e2;margin-top:6px}
  .bio p{font-size:9.2px;line-height:1.38;margin-top:12px}

  /* inside – services panels */
  .services{position:absolute;left:22px;right:18px}
  .services h2{color:var(--purple);font-size:21px;margin-bottom:12px}
  .service-row{display:flex;align-items:center;gap:12px;margin-bottom:10px;font-size:10px;color:var(--muted)}
  .service-icon{width:34px;height:30px;border-radius:8px;background:var(--purple);flex:none;display:flex;align-items:center;justify-content:center}
  .intro{font-size:10px;color:var(--muted);line-height:1.4}
  .it-title{font-family:"Ubuntu",sans-serif;font-weight:700;font-style:italic;font-size:15px;color:var(--purple);margin:12px 0 6px}
  .it-list{list-style:none;font-size:10px;color:var(--muted)}
  .it-list li{display:flex;align-items:center;gap:7px;margin-bottom:5px}
  .it-list li::before{content:"";width:7px;height:7px;border:1.3px solid var(--muted);border-radius:50%;flex:none}
  .url-band{position:absolute;right:0;bottom:0;width:220px;height:68px;background:var(--purple);border-radius:44px 0 0 0;color:#fff;font-size:11px;letter-spacing:1.5px;display:flex;align-items:center;justify-content:center}
</style>
</head>
<body>

<section class="sheet sheet--outside" aria-label="Brochure outside">
  <div class="panel panel--about">
    <div class="photo" role="img" aria-label="Photo of colleagues reviewing charts at a desk" style="left:0;top:0;width:100%;height:250px;background:linear-gradient(150deg,#d9d3c6,#7d7668 60%,#3e3c3a)"></div>
    <svg class="wave" style="top:205px" height="70" viewBox="0 0 298 70" preserveAspectRatio="none"><path d="M0 70 L0 40 C90 45 200 30 298 0 L298 70 Z" fill="#fff"/><path d="M0 70 L0 48 C90 52 200 36 298 8 L298 20 C200 46 100 62 0 70Z" fill="var(--purple)"/></svg>
    <h2 class="about-tab">About Us</h2>
    <div class="about-body">
      <h3>Our Mission</h3>
      <p>Partner with clients to increase the value and security of their technology tools.</p>
      <h3>Our Goal</h3>
      <p>Become the premiere consulting company for Information Technology in the post-acute care industries.</p>
      <h3>Our Leaders</h3>
      <p class="leader"><b>Dana Whitford</b>, MHA, MBA</p>
    </div>
    <svg class="wave" style="bottom:0" height="40" viewBox="0 0 298 40" preserveAspectRatio="none"><path d="M0 20 C100 30 200 20 298 0 L298 40 L0 40Z" fill="var(--purple)"/></svg>
  </div>

  <div class="panel panel--contact">
    <div class="badge" aria-label="Partner badge"></div>
    <svg class="wave" style="top:112px" height="30" viewBox="0 0 298 30" preserveAspectRatio="none"><path d="M0 30 C100 10 200 0 298 0 L298 10 C200 12 100 20 0 30Z" fill="var(--purple)"/></svg>
    <div class="photo" role="img" aria-label="Illustration of a clinician with medical icons in a hexagon grid" style="left:0;top:135px;width:100%;height:195px;background:linear-gradient(120deg,#eef3f7,#b9cfde 55%,#4f7fa6)"></div>
    <div class="contact">
      <h2>Contact Us</h2>
      <div class="phone">
        <svg width="18" height="18" viewBox="0 0 24 24"><circle cx="12" cy="12" r="11" fill="#fff"/><path d="M8 6.5l2 0 1 3-1.5 1a7 7 0 003 3l1-1.5 3 1v2a1.5 1.5 0 01-1.6 1.5A11 11 0 016.5 8.1 1.5 1.5 0 018 6.5z" fill="var(--purple)"/></svg>
        515-555-0148
      </div>
      <div class="email">
        <svg width="12" height="12" viewBox="0 0 12 12"><circle cx="6" cy="6" r="6" fill="#fff"/><rect x="3" y="4" width="6" height="4" fill="var(--purple)"/></svg>
        dwhitford@brevalinkpro.com
      </div>
    </div>
  </div>

  <div class="panel panel--cover">
    <div class="brand"><span class="brand-mark"></span><span class="brand-name">BrevaLink Pro</span></div>
    <svg class="wave" style="top:88px" height="40" viewBox="0 0 298 40" preserveAspectRatio="none"><path d="M0 0 C90 0 180 10 298 40 L298 30 C180 4 90 -4 0 0Z" fill="var(--purple)"/></svg>
    <div class="headline">
      <h1>Increasing The Value and Security of Your Technology Resources</h1>
      <p>Providing Information Technology expertise to post-acute care providers</p>
    </div>
    <div class="photo" role="img" aria-label="Photo of a business team in a relaxed meeting" style="left:0;top:262px;width:100%;height:220px;background:linear-gradient(140deg,#c8d7a4,#8c8a7c 45%,#3b3a44)"></div>
    <svg class="wave" style="bottom:0" height="90" viewBox="0 0 298 90" preserveAspectRatio="none"><path d="M0 40 C100 70 200 40 298 10 L298 90 L0 90Z" fill="var(--purple)"/></svg>
  </div>
</section>

<section class="sheet sheet--inside" aria-label="Brochure inside">
  <div class="panel panel--bio">
    <div class="photo" role="img" aria-label="Photo of a professional working on a laptop and phone" style="left:0;top:0;width:100%;height:220px;background:linear-gradient(150deg,#f1eeee,#d4c7c4 55%,#8f7e7a)"></div>
    <svg class="wave" style="top:198px" height="55" viewBox="0 0 298 55" preserveAspectRatio="none"><path d="M0 30 L298 20 L298 55 L0 55Z" fill="var(--purple-soft)"/><path d="M0 42 L298 34 L298 55 L0 55Z" fill="var(--purple)"/></svg>
    <div class="bio">
      <div class="bio-head">
        <div class="portrait" role="img" aria-label="Portrait of the company president"></div>
        <div>
          <div class="bio-name">Dana Whitford, <small>MHA, MBA, CHCIO</small></div>
          <div class="bio-role">President and CEO</div>
          <div class="bio-badge" aria-label="Partner badge"></div>
        </div>
      </div>
      <p>Dana is the founder and CEO of BrevaLink Pro Solutions. Dana has been working in the technology industry for over 25 years with extensive experience in healthcare IT. Dana has held multiple roles including Chief Information Officer, Chief Information Security Officer, and the executive sponsor of multiple electronic health record (EHR) implementations. Dana has created and nurtured numerous successful IT departments and built strong relationships with leadership teams. Dana holds a Master's in Business Administration and a Master's in Healthcare Administration, and is certified with the Healthcare Information Leadership Council (HILC).</p>
    </div>
  </div>

  <div class="panel panel--values">
    <div class="photo" role="img" aria-label="Photo of hands typing on a laptop keyboard" style="left:20px;top:14px;width:258px;height:150px;border-radius:34px;border:6px solid var(--purple-soft);background:linear-gradient(150deg,#eef0f4,#b6bcc8 55%,#5c6170)"></div>
    <svg class="wave" style="top:170px" height="40" viewBox="0 0 298 40" preserveAspectRatio="none"><path d="M0 40 C90 10 200 0 298 10 L298 0 L0 0Z" fill="#fff"/><path d="M0 40 C90 12 200 2 298 14 L298 20 C200 10 90 20 0 40Z" fill="var(--purple)"/></svg>
    <div class="services" style="top:218px">
      <h2>Our Services</h2>
      <div class="service-row"><span class="service-icon"><svg width="16" height="16" viewBox="0 0 16 16"><circle cx="8" cy="8" r="6" fill="none" stroke="#fff" stroke-width="1.6"/><path d="M5 8l2 2 4-4" fill="none" stroke="#fff" stroke-width="1.6"/></svg></span>Understand and exceed client expectations</div>
      <div class="service-row"><span class="service-icon"><svg width="18" height="14" viewBox="0 0 18 14"><path d="M1 7l4-4 4 3 4-3 4 4-6 5z" fill="none" stroke="#fff" stroke-width="1.5"/></svg></span>Committed to be a partner, not vendor</div>
      <div class="service-row"><span class="service-icon"><svg width="16" height="16" viewBox="0 0 16 16"><circle cx="8" cy="5" r="3" fill="#fff"/><path d="M2 15c0-4 3-5 6-5s6 1 6 5z" fill="#fff"/></svg></span>Provide simplified change management expertise</div>
    </div>
    <div class="photo" role="img" aria-label="Photo of medical staff in white coats reviewing work" style="left:0;bottom:0;width:100%;height:170px;background:linear-gradient(140deg,#e9eef2,#c4cfd6 50%,#7d8a96)"></div>
  </div>

  <div class="panel panel--it">
    <div class="photo" role="img" aria-label="Illustration of a hand touching a digital IT hexagon interface" style="left:0;top:0;width:100%;height:150px;background:linear-gradient(140deg,#7f9db8,#3e5e82 55%,#1f3452)"></div>
    <svg class="wave" style="top:110px" height="50" viewBox="0 0 298 50" preserveAspectRatio="none"><path d="M0 50 C100 10 200 0 298 20 L298 50Z" fill="#fff"/><path d="M0 50 C100 6 200 -4 298 14 L298 24 C200 6 100 14 0 50Z" fill="var(--purple)"/></svg>
    <div class="services" style="top:172px">
      <h2>Our Services</h2>
      <p class="intro">We understand different organizations have different needs. BrevaLink Pro strives to assist your organization by bringing solutions that are easy to understand and allow the client to track success. We provide solutions based on the client's needs and desires.</p>
      <div class="it-title">Information Technology</div>
      <ul class="it-list">
        <li>CIO or IT Director Services</li>
        <li>CISO or Information Security Officer</li>
        <li>Comprehensive ePHI Risk Assessments</li>
        <li>IT Department Evaluation</li>
        <li>Policy Management and Consulting</li>
        <li>On-going IT department support</li>
      </ul>
    </div>
    <div class="url-band">www.brevalinkpro.com</div>
  </div>
</section>

</body>
</html>
```